A 'new law' boutique Australian law firm that provides specialist employment law and people managem

We value helping clients create results with respect workplaces. What differentiates us is we provide actionable training in understanding and dealing with people and ensure legal compliance fits with this approach. We would like a fresh approach to our training overview documents that we currently use in our current law firm (6 attached). Please use pictures, symbols etc consistent with our non-traditional law approach that captures the approach of each training session.. Attached is the logo and draft letterhead for Brindle Legal which will launch soon.

Target Market(s)

HR Managers and in-house lawyers (non employment specialists) in mid-large Australian companies that are progressive with a relationship based approach to managing employee behaviours and disputes.

Industry/Entity Type

Human Resource

Font styles to use
Sans Serif

Colors
3176b5
33a6d7

Requirements
Must have
• 1 or 2 page PDF for each of the 6 documents that the wording supplied goes into your design which will be pretty similar as we want consistency with our documents

```html
<!DOCTYPE html>
<html lang="en">
<head>
<meta charset="utf-8">
<title>Brindle Legal – Managing Performance Training Overview</title>
<link href="https://fonts.googleapis.com/css2?family=Open+Sans:wght@400;600;700&display=swap" rel="stylesheet">
<style>
:root{
  --blue:#3176b5;
  --sky:#33a6d7;
  --ink:#4a4a4a;
  --muted:#7a7a7a;
  --grey-band:#8a8a8a;
  --row-light:#ececec;
  --row-dark:#c6c6c6;
  --stage:#e4e6e8;
  --paper:#ffffff;
}
*{box-sizing:border-box;margin:0;padding:0}
html,body{width:1200px;height:800px;overflow:hidden}
body{background:var(--stage);font-family:'Open Sans',sans-serif;color:var(--ink);position:relative}

.page{position:absolute;top:18px;width:537px;height:764px;background:var(--paper);box-shadow:0 4px 14px rgba(0,0,0,.18);overflow:hidden}
.page--overview{left:46px}
.page--cover{left:617px}

/* ---------- overview page ---------- */
.overview-body{padding:34px 30px 0}
.section-title{display:flex;align-items:center;gap:8px;font-size:11.5px;font-weight:700;color:var(--blue);letter-spacing:.3px;margin-bottom:6px}
.section-title::after{content:"";flex:1;height:1px;background:var(--blue);opacity:.6}
.section-title .accent{color:var(--sky);font-weight:600}

.training-table{width:100%;border-collapse:collapse;font-size:7.6px;line-height:1.25}
.training-table td{padding:6px 8px;vertical-align:middle;border-bottom:2px solid #fff}
.training-table td.topic{width:38%;color:#555;border-right:2px solid #fff}
.training-table tr:nth-child(odd) td{background:var(--row-light)}
.training-table tr:nth-child(even) td{background:var(--row-dark)}
.training-table ul{list-style:none}
.training-table li::before{content:"• ";}
.training-table b{font-weight:700;color:#333}

.outcomes{margin-top:14px}
.outcomes p.lead{font-size:7.8px;color:var(--muted);margin-bottom:6px}
.outcomes ol{font-size:7.8px;color:var(--muted);padding-left:14px;line-height:1.3}
.outcomes ol li{margin-bottom:5px}
.outcomes ol li::marker{color:var(--blue);font-weight:700}

.overview-footer{position:absolute;left:0;right:0;bottom:0;height:170px;background:linear-gradient(#f1f1f1,#d9d9d9);padding:34px 30px}
.wordmark{display:flex;align-items:center;gap:8px}
.wordmark .dot{width:12px;height:12px;border-radius:2px;background:var(--blue)}
.wordmark .name{font-size:24px;font-weight:600;color:var(--blue);letter-spacing:.2px}
.tagline{font-size:7.5px;color:#666;letter-spacing:.6px;margin-top:3px}
.abn{font-size:7.5px;color:#666;margin-top:10px}
.office-list{position:absolute;right:30px;top:26px;text-align:right;font-size:9px;color:#555;line-height:1.5}
.office-list .office{margin-bottom:12px}

/* ---------- cover page ---------- */
.hero{position:absolute;left:0;top:0;width:100%;height:262px;background:linear-gradient(135deg,#dfe8f2 0%,#b6c7da 45%,#8fa3ba 100%)}
.cover-panel{position:absolute;left:0;top:0;width:100%;height:100%}
.cover-content{position:absolute;left:0;top:0;width:100%;height:100%}
.headline{position:absolute;left:28px;top:218px}
.headline .kicker{font-size:14px;font-weight:700;color:#555;letter-spacing:.5px}
.headline .title{font-size:18px;font-weight:400;color:var(--blue);letter-spacing:.4px;margin-top:1px}
.columns{position:absolute;left:28px;right:26px;top:282px;display:grid;grid-template-columns:1fr 1fr;gap:26px;font-size:8.7px;line-height:1.32;color:#555}
.columns p{margin-bottom:9px}
.columns .faint{color:#999}
.cover-logo{margin-top:24px}

.cover-footer{position:absolute;left:0;bottom:0;width:100%;height:56px}
.footer-band{position:absolute;inset:0;width:100%;height:100%}
.contact-links{position:absolute;left:30px;top:10px;font-size:9px;color:#fff;line-height:1.65}
.contact-links div,.social-links div{display:flex;align-items:center;gap:6px}
.contact-links .icon{flex:none;width:10px;height:10px}
.social-links{position:absolute;right:40px;top:10px;font-size:9px;color:#fff;line-height:1.65}
.social-links .mark{width:9px;height:9px;border-radius:50%;background:#fff}
</style>
</head>
<body>

<!-- Page 2: training overview -->
<article class="page page--overview">
  <div class="overview-body">
    <h2 class="section-title">OVERVIEW OF TRAINING</h2>
    <table class="training-table">
      <tr>
        <td class="topic">Understanding the current problem with performance management</td>
        <td><ul>
          <li>4 common types of poor performing employees</li>
          <li>4 common types of ineffective managers</li>
          <li>Commonly arising legal claims and their typical resolution arising out of our common types of poor performers and their ineffective managers</li>
        </ul></td>
      </tr>
      <tr>
        <td class="topic">3 Step approach for managing performance: build relationships, have crucial conversations, and make right decisions</td>
        <td><ul>
          <li><b>Build Relationships</b> by bringing managerial authority to get compliance and know your people to get trust and commitment</li>
          <li>How to have effective One on Ones</li>
          <li>How to give Frequent Feedback</li>
          <li>What is Line Manager's Intent and how to communicate it</li>
          <li><b>Have Crucial Conversations</b> using a 3-step approach</li>
          <li>How to frame performance issues</li>
          <li>Performance and frame collision</li>
          <li>Low versus High Intensity Crucial Conversations</li>
          <li>Using emails to support crucial conversations</li>
          <li>What are <b>Right Decisions</b> and how to make them</li>
        </ul></td>
      </tr>
      <tr>
        <td class="topic">Understanding DISC</td>
        <td><ul>
          <li>Introduction to DISC</li>
          <li>Explanation of DISC styles</li>
          <li>Interpreting DISC styles from verbal, vocal and visual behaviours</li>
        </ul></td>
      </tr>
      <tr>
        <td class="topic">Applying DISC to the workplace</td>
        <td><ul>
          <li>Understanding how each DISC style impacts on communication in the workplace</li>
          <li>Tips and traps of the DISC styles and how they can create/resolve workplace conflict</li>
        </ul></td>
      </tr>
      <tr>
        <td class="topic">Putting it into practice</td>
        <td>Practice by <b>role playing</b> crucial conversations and creating crucial emails for tailored hypothetical workplace scenarios with escalating problem employees and their managers</td>
      </tr>
    </table>

    <section class="outcomes">
      <h2 class="section-title">LEARNING <span class="accent">OUTCOMES</span></h2>
      <p class="lead">Training utilises activities to apply the tools taught, to enable HR (who will enable managers to):</p>
      <ol>
        <li>understand what is Managerial Authority, why it is fundamental to being a manager and cannot be outsourced to HR, and how to bring it;</li>
        <li>use DISC to understand your Management style and the how to adjust your style so people will genuinely be open to performance conversations;</li>
        <li>learn 'performance framing' to achieve results or respectfully remove employees by 'self-selecting' or consequences with no surprises;</li>
        <li>focus on Making the Right Decisions which are often the hard, right decisions not the easy, wrong ones. Crucial conversations must be backed up with crucial judgment calls; and</li>
        <li>implement crucial conversations supported by emails to effectively 'build your case'. That way there is only one process which is either low or high intensity removing the artificial distinction of formal and informal processes and separate legal processes.</li>
      </ol>
    </section>
  </div>

  <footer class="overview-footer">
    <div class="wordmark"><span class="dot"></span><span class="name">Brindle Legal</span></div>
    <div class="tagline">EMPLOYMENT &amp; PEOPLE LAW</div>
    <div class="abn">ABN 12 345 678 90</div>
    <div class="office-list">
      <div class="office">41 Harbour Lane<br>Hobart 7000<br>(03) 55xx xxxx</div>
      <div class="office">12 Carrow St Melbourne 3000<br>(03) xxxx xxxx</div>
    </div>
  </footer>
</article>

<!-- Page 1: cover -->
<article class="page page--cover">
  <div class="hero" role="img" aria-label="Photo of a team of colleagues meeting around a table in a bright office"></div>
  <svg class="cover-panel" viewBox="0 0 537 764" aria-hidden="true">
    <defs>
      <linearGradient id="panelFill" x1="0" y1="0" x2="0" y2="1">
        <stop offset="0" stop-color="#ffffff"/>
        <stop offset=".35" stop-color="#f4f4f4"/>
        <stop offset="1" stop-color="#e6e6e6"/>
      </linearGradient>
    </defs>
    <path d="M0 205 H290 Q310 205 316 226 L322 244 Q328 262 350 262 H537 V764 H0 Z" fill="url(#panelFill)"/>
  </svg>

  <div class="cover-content">
    <div class="headline">
      <div class="kicker">MANAGING PERFORMANCE:</div>
      <div class="title">CRUCIAL CONVERSATIONS</div>
    </div>

    <div class="columns">
      <div>
        <p class="faint">HR teams deal with increasing Workplace Tribunal intervention when managing performance because of changes to laws, constant workplace change and increasing awareness of rights.</p>
        <p class="faint">Reliance on complex processes such as formal performance improvement plans don't work - if they did they would be used on top performers as well as poor performers.</p>
        <p>Reliance on warning letters does not get performance results and often does not build the case to remove poor performers and avoid the risk of successful legal claims. Many workplace investigations of complaints are nothing more than unaddressed poor performance issues over time.</p>
        <p>The solution is to manage most workplace behaviours as performance through meaningful, regular performance discussions (supported by email) and not complex performance or disciplinary processes.</p>
      </div>
      <div>
        <p>Technology hasn't replaced the need and want for conversations. This is achieved by simple and streamlined processes enabling managers to be responsible for effectively managing their team members (with HR support) and to continue in the face of any claims made during these processes.</p>
        <p>This will get you results or removal with respect.</p>
        <p>DISC is a behavioural style tool that is easy to apply and highly effective in the workplace for effective communication and building relationships. We are accredited DISC Trainers and apply this tool in all our workshops.</p>
        <div class="cover-logo">
          <div class="wordmark"><span class="dot"></span><span class="name">Brindle Legal</span></div>
          <div class="tagline">EMPLOYMENT &amp; PEOPLE LAW</div>
        </div>
      </div>
    </div>
  </div>

  <footer class="cover-footer">
    <svg class="footer-band" viewBox="0 0 537 56" preserveAspectRatio="none" aria-hidden="true">
      <rect width="537" height="56" fill="#8a8a8a"/>
      <polygon points="0,0 340,0 300,56 0,56" fill="#3176b5"/>
      <polygon points="340,0 352,0 312,56 300,56" fill="#ffffff"/>
    </svg>
    <div class="contact-links">
      <div>
        <svg class="icon" viewBox="0 0 10 10" aria-hidden="true"><circle cx="5" cy="5" r="4.3" fill="none" stroke="#fff"/><path d="M0.8 5H9.2M5 0.8C3 3 3 7 5 9.2M5 0.8C7 3 7 7 5 9.2" fill="none" stroke="#fff" stroke-width=".7"/></svg>
        <span>www.brindlelegal.com.au</span>
      </div>
      <div>
        <svg class="icon" viewBox="0 0 10 10" aria-hidden="true"><rect x="0.5" y="2" width="9" height="6.5" rx="1" fill="none" stroke="#fff"/><path d="M0.8 2.4L5 5.8L9.2 2.4" fill="none" stroke="#fff" stroke-width=".8"/></svg>
        <span>info@brindlelegal.com.au</span>
      </div>
    </div>
    <div class="social-links">
      <div><span class="mark"></span>brindlelegal</div>
      <div><span class="mark"></span>brindlelegal</div>
    </div>
  </footer>
</article>

</body>
</html>
```